Interior Design/ decoration business card design

This card is for my Interior Design and Decoration business and later I will also be selling homewares. I would like the card to be very simple in design and like either white, duck egg blue , aquas or metallics on a flat mat card excellent quality card. It needs to be well designed as that is my field. I dont like fuss, the simpler the better. I would like a styalised wren under the name wren if possible. SIMPLE, STYLISH, CLASSIC, TASTEFUL

Target Market(s)

40 + year olds who are building or rennovating.

Industry/Entity Type

Business

Contact Information for Business Card

Wren
styling, design, homeware

Marnie Tolland
p 0427316958
e marnie@wrenliving.com.au
w wrenliving.com.au

Requirements
Must have
• very simple, stylish, classic, sophisticated. Simple and easy to read text that is a print similar to attached image. I like simple round A's though not as in attached image.

Double sided. It wont save as double sided for some reason!!
Should not have
• not too much colour, No animated / cartoon pictures.

```html
<!DOCTYPE html>
<html lang="en">
<head>
<meta charset="utf-8">
<title>Wren — business card</title>
<link rel="stylesheet" href="https://fonts.googleapis.com/css2?family=Arimo:wght@400;700&display=swap">
<style>
  :root {
    --backdrop: #e8e6e3;
    --card: #ffffff;
    --duck-egg: #a9d3cf;
    --ink: #3b3532;
    --ink-strong: #111111;
    --icon: #ffffff;
  }
  * { box-sizing: border-box; margin: 0; padding: 0; }
  html, body {
    width: 1200px; height: 592px; overflow: hidden;
    background: var(--backdrop);
    font-family: "Arimo", Arial, sans-serif;
    color: var(--ink);
  }
  .sheet {
    position: relative; width: 1200px; height: 592px;
    display: flex; justify-content: center; align-items: center; gap: 80px;
  }
  .card {
    position: relative; width: 500px; height: 305px;
    background: var(--card); border-radius: 18px; overflow: hidden;
    box-shadow: 0 2px 8px rgba(0,0,0,0.12);
  }
  .card__band {
    position: absolute; top: 0; bottom: 0; width: 56px;
    background: var(--duck-egg);
  }
  .card--front .card__band { right: 0; }
  .card--back .card__band { left: 0; width: 46px; }

  .brand { display: flex; flex-direction: column; align-items: center; }
  .brand__name {
    display: flex; align-items: center; gap: 10px;
    font-size: 50px; font-weight: 400; letter-spacing: 1px; line-height: 1;
    color: var(--ink);
  }
  .brand__dot {
    width: 10px; height: 10px; border-radius: 50%; background: var(--ink);
  }
  .brand__tagline {
    margin-top: 22px; font-size: 17px; letter-spacing: 0.3px;
    display: flex; align-items: center;
  }
  .brand__tagline span + span {
    border-left: 2px solid var(--ink); margin-left: 5px; padding-left: 5px;
    line-height: 1;
  }

  .card--front .brand {
    position: absolute; left: 0; right: 56px; top: 96px;
  }

  .card--back .brand {
    position: absolute; right: 36px; bottom: 48px;
  }
  .card--back .brand__name { font-size: 38px; }
  .card--back .brand__tagline { margin-top: 16px; font-size: 13px; }

  .holder { position: absolute; left: 76px; top: 34px; }
  .holder__name { font-size: 17px; font-weight: 700; color: var(--ink-strong); }
  .holder__role { font-size: 11px; font-weight: 700; color: var(--ink-strong); margin-top: 2px; }

  .contact-icons {
    position: absolute; left: 0; width: 46px; top: 104px;
    display: flex; flex-direction: column; align-items: center; gap: 10px;
  }
  .contact-icons svg { width: 16px; height: 16px; display: block; }

  .contact-list {
    position: absolute; left: 76px; top: 110px; list-style: none;
    font-size: 14px; line-height: 24px; color: var(--ink-strong);
  }
</style>
</head>
<body>
<main class="sheet">
  <section class="card card--front" aria-label="Card front">
    <div class="brand">
      <div class="brand__name"><span>wren</span><span class="brand__dot"></span></div>
      <div class="brand__tagline"><span>decoration</span><span>styling</span><span>homeware</span></div>
    </div>
    <div class="card__band"></div>
  </section>

  <section class="card card--back" aria-label="Card back">
    <div class="card__band"></div>
    <div class="contact-icons">
      <svg viewBox="0 0 16 16" aria-label="Phone" role="img">
        <rect x="3.5" y="1" width="9" height="14" rx="1.5" fill="none" stroke="var(--icon)" stroke-width="1.2"/>
      </svg>
      <svg viewBox="0 0 16 16" aria-label="Email" role="img">
        <rect x="1" y="3.5" width="14" height="9" fill="none" stroke="var(--icon)" stroke-width="1.2"/>
        <path d="M1 3.5 L8 9 L15 3.5" fill="none" stroke="var(--icon)" stroke-width="1.2"/>
      </svg>
      <svg viewBox="0 0 16 16" aria-label="Website" role="img">
        <circle cx="8" cy="8" r="6.5" fill="none" stroke="var(--icon)" stroke-width="1.2"/>
        <path d="M1.5 8 H14.5 M8 1.5 C5 5 5 11 8 14.5 M8 1.5 C11 5 11 11 8 14.5" fill="none" stroke="var(--icon)" stroke-width="1"/>
      </svg>
    </div>
    <div class="holder">
      <p class="holder__name">Marnie Tolland</p>
      <p class="holder__role">Homeware Expert</p>
    </div>
    <ul class="contact-list">
      <li>0427316958</li>
      <li>marnie@wrenliving.com.au</li>
      <li>wrenliving.com.au</li>
    </ul>
    <div class="brand">
      <div class="brand__name"><span>wren</span><span class="brand__dot"></span></div>
      <div class="brand__tagline"><span>decoration</span><span>styling</span><span>homeware</span></div>
    </div>
  </section>
</main>
</body>
</html>
```